Labour Hire App - Screen and Logo Design

I have about 15-30 screens I need designed. They are pretty basic as long as they follow the same style guide.
I've got rough wire framing I just need a logo, style guide & screens designed.

The idea behind the app is to provide workplaces and workers a quick and easy solution to their labour and equipment needs.

Target Market(s)

Construction and labour force

Industry/Entity Type

Construction

Font styles to use
Serif

Colors
faa54b
f37122
abd037
9bcb3c

Requirements
Must have
• Each of the displayed screens need to be represented.

```html
<!DOCTYPE html>
<html lang="en">
<head>
<meta charset="utf-8">
<title>KORVA – Thank You</title>
<link rel="stylesheet" href="https://fonts.googleapis.com/css2?family=Open+Sans:wght@400&family=Cormorant+Garamond:wght@500&display=swap">
<style>
  :root {
    --canvas: #ffffff;
    --panel: #9ecb3c;
    --panel-edge: #3c4a1a;
    --ink: #111111;
    --white: #ffffff;
    --orange: #f37122;
    --orange-light: #faa54b;
  }
  * { margin: 0; padding: 0; box-sizing: border-box; }
  html, body {
    width: 1200px;
    height: 960px;
    overflow: hidden;
    background: var(--canvas);
  }
  .canvas {
    position: relative;
    width: 1200px;
    height: 960px;
  }
  .screen {
    position: absolute;
    left: 293px;
    top: 128px;
    width: 614px;
    height: 704px;
    background: var(--panel);
    border: 1px solid var(--panel-edge);
    font-family: "Open Sans", sans-serif;
    color: var(--ink);
  }
  .thanks {
    position: absolute;
    top: 236px;
    width: 100%;
    text-align: center;
    font-size: 21px;
    line-height: 1;
  }
  .wordmark {
    position: absolute;
    top: 288px;
    width: 100%;
    text-align: center;
    font-family: "Cormorant Garamond", serif;
    font-weight: 500;
    font-size: 128px;
    line-height: 1;
    letter-spacing: 4px;
    color: var(--white);
  }
  .tagline {
    position: absolute;
    top: 438px;
    width: 100%;
    text-align: center;
    font-size: 16px;
    line-height: 1;
  }
  .home-link {
    position: absolute;
    top: 560px;
    left: 0;
    width: 100%;
    text-align: center;
  }
  .home-link a {
    display: inline-block;
    font-size: 16px;
    line-height: 1;
    color: var(--ink);
    text-decoration: none;
    padding-bottom: 3px;
    border-bottom: 2px solid var(--white);
  }
  .back {
    position: absolute;
    left: 470px;
    top: 638px;
    display: flex;
    align-items: center;
    gap: 0;
    color: var(--ink);
    text-decoration: none;
    font-size: 17px;
    line-height: 1;
  }
  .back svg { display: block; margin-right: -6px; }
</style>
</head>
<body>
  <div class="canvas">
    <main class="screen">
      <p class="thanks">Thank you for using</p>
      <h1 class="wordmark">KORVA</h1>
      <p class="tagline">The best in Human and Equipment Resourses</p>
      <div class="home-link"><a href="#">Thake me back to the Home page</a></div>
      <a class="back" href="#">
        <svg width="28" height="31" viewBox="0 0 28 31" aria-hidden="true">
          <polygon points="14,0 28,0 14,15.5 28,31 14,31 0,15.5" fill="var(--orange)"/>
        </svg>
        <span>go back</span>
      </a>
    </main>
  </div>
</body>
</html>
```